Velmora Partners - website for real estate investment company

Create a bold, modern website that reflects Velmora’s success, professionalism, and credibility.
The design must stand out while maintaining a polished, corporate tone. (bold, but understated)
The client just created a new logo, and the website design must be in sync with the logo design. Information about the logo colors, fonts, and message are in the attached design brief.
Updates

Target Market(s)

b2b: banks, brokers, institutional partners, vendors, and property sellers.

Industry/Entity Type

real estate investment company

Number of Pages Required

1 page

Font styles to use
Sans Serif

Colors

Designer to choose colors to be used in the design.

Requirements
Must have
• 1. homepage design (psd) 2. a top banner image (psd) for a default inner page
Nice to have
• please see attached design brief
Should not have

```html
<!DOCTYPE html>
<html lang="en">
<head>
<meta charset="utf-8">
<title>Velmora Partners — Real Estate Investment</title>
<link href="https://fonts.googleapis.com/css2?family=Oswald:wght@400;500;600;700&family=Montserrat:wght@400;500;600;700&display=swap" rel="stylesheet">
<style>
:root{
  --red:#e21d25;
  --dark:#26282b;
  --ink:#2f3236;
  --text:#4a4d52;
  --muted:#8b8e93;
  --line:#d9dadc;
  --white:#ffffff;
}
*{box-sizing:border-box;margin:0;padding:0}
html,body{width:1200px;height:4501px;overflow:hidden;background:var(--white)}
body{font-family:'Montserrat',sans-serif;color:var(--text);position:relative}
.abs{position:absolute}
.head-font{font-family:'Oswald',sans-serif;text-transform:uppercase}
.photo{position:absolute}
/* buttons */
.btn{position:absolute;height:32px;background:var(--white);color:var(--red);font-size:11px;font-weight:600;display:flex;align-items:center;justify-content:center;border-bottom:2px solid var(--red);box-shadow:0 2px 6px rgba(0,0,0,.12)}
.btn::after{content:"";position:absolute;right:0;top:0;width:18px;height:100%;background:var(--red);clip-path:polygon(100% 0,100% 100%,0 100%)}
.btn.on-red{background:var(--white)}
/* header */
.site-header{position:absolute;top:0;left:0;width:1200px;height:65px;background:var(--white);border-bottom:1px solid #eee;z-index:3}
.brand{position:absolute;font-family:'Oswald',sans-serif;font-weight:700;color:var(--ink);letter-spacing:1px}
.nav{position:absolute;left:300px;top:0;height:65px;display:flex;align-items:center;gap:33px;font-size:12px;color:var(--ink)}
.nav .active{color:var(--red)}
.header-phone{position:absolute;left:872px;top:25px;font-size:12px;font-weight:600;color:var(--red);display:flex;align-items:center;gap:6px}
.header-search{position:absolute;left:842px;top:24px}
.header-cta{position:absolute;left:988px;top:17px;width:112px;height:34px;background:var(--red);color:var(--white);font-size:12px;font-weight:600;display:flex;align-items:center;justify-content:center;box-shadow:3px 3px 0 #b5141b}
/* hero */
.hero{position:absolute;top:65px;left:0;width:1200px;height:550px;overflow:hidden;background:linear-gradient(180deg,#e9a07e 0%,#c98c86 20%,#7d7a84 45%,#4b4d55 70%,#2d2f35 100%)}
.hero-shade{position:absolute;inset:0;background:linear-gradient(90deg,rgba(20,20,24,.75) 0%,rgba(20,20,24,.45) 40%,rgba(20,20,24,0) 70%)}
.hero-wedge{position:absolute;left:0;top:0;width:330px;height:270px;background:var(--red);clip-path:polygon(0 0,100% 0,0 100%);opacity:.95}
.hero-title{position:absolute;left:100px;top:72px;font-family:'Oswald',sans-serif;font-weight:700;font-size:58px;line-height:65px;color:var(--white);text-transform:uppercase}
.hero-title span{display:inline-block;padding:0 4px;margin-left:-4px}
.hero-title .hl{background:var(--red)}
.hero-copy{position:absolute;left:100px;top:355px;width:390px;font-size:11px;line-height:17px;color:var(--white)}
/* stats */
.stat{position:absolute;top:660px;width:280px;text-align:center}
.stat b{display:block;font-family:'Oswald',sans-serif;font-weight:500;font-size:40px;color:var(--red);line-height:48px;text-transform:uppercase}
.stat span{display:block;font-size:14px;color:var(--text);margin-top:16px}
.stat-divider{position:absolute;top:660px;width:2px;height:110px;background:var(--line)}
/* section heading */
.sec-title{position:absolute;font-family:'Oswald',sans-serif;font-weight:500;font-size:42px;color:var(--ink);text-transform:uppercase;line-height:50px;display:flex;align-items:center;gap:16px}
.sec-title .rule{display:inline-block;width:84px;height:3px;background:var(--red)}
.sec-title.center{left:0;width:1200px;justify-content:center;gap:20px}
/* about */
.about-photo{left:109px;top:830px;width:530px;height:393px;background:linear-gradient(135deg,#4d5358 0%,#8c9599 40%,#c9cfd1 70%,#e7eaeb 100%)}
.frame-tl{position:absolute;left:100px;top:821px;width:230px;height:180px;border-top:9px solid var(--red);border-left:9px solid var(--red)}
.frame-br{position:absolute;left:416px;top:1052px;width:230px;height:180px;border-bottom:9px solid var(--red);border-right:9px solid var(--red)}
.about-text{position:absolute;left:683px;top:904px;width:420px;font-size:12px;line-height:19px;color:var(--text)}
.about-text p{margin-bottom:11px}
.about-text strong{color:var(--ink)}
.ghost-word{position:absolute;left:1126px;top:870px;font-family:'Oswald',sans-serif;font-weight:700;font-size:78px;color:#efeff0;transform:rotate(-90deg);transform-origin:left top;white-space:nowrap;letter-spacing:2px;top:1160px}
/* portfolio */
.portfolio-band{position:absolute;left:0;top:1310px;width:1200px;height:329px;background:linear-gradient(90deg,#2b2d31 0%,#3b3e43 50%,#2b2d31 100%)}
.portfolio-arrows{position:absolute;left:638px;top:1310px;width:104px;height:88px;background:var(--red)}
.arrow-box{position:absolute;top:20px;width:30px;height:30px;background:var(--white);display:flex;align-items:center;justify-content:center}
.portfolio-copy{position:absolute;left:100px;top:1450px;width:360px;font-size:12px;line-height:19px;color:#e6e6e6}
.card-photo{top:1398px;height:300px}
.card-cap{position:absolute;top:1713px;font-family:'Oswald',sans-serif;font-size:14px;line-height:22px;color:var(--ink);text-transform:uppercase;white-space:nowrap}
/* approach */
.approach-col{position:absolute;top:1905px;width:290px;text-align:center}
.approach-col svg{display:block;margin:0 auto}
.approach-col h3{font-family:'Oswald',sans-serif;font-weight:500;font-size:15px;color:var(--ink);text-transform:uppercase;margin-top:22px}
.approach-col p{font-size:12px;line-height:19px;color:var(--ink);margin-top:12px}
/* pillars */
.pillar{top:2212px;height:505px}
.pillar-cap{position:absolute;top:2606px;width:400px;text-align:center;color:var(--white)}
.pillar-cap h4{font-family:'Oswald',sans-serif;font-weight:500;font-size:15px;text-transform:uppercase}
.pillar-cap p{font-size:12px;line-height:19px;margin-top:10px}
.pillar-cap i{display:block;width:86px;height:2px;background:var(--red);margin:14px auto 0}
/* partners */
.badge{position:absolute;top:2790px;width:80px;height:72px;display:flex;flex-direction:column;align-items:center;gap:8px}
.badge .mark{width:44px;height:44px;background:#6f7276;border-radius:50%}
.badge .mark.sq{border-radius:2px}
.badge .bar{width:76px;height:6px;background:#a9abae}
/* news */
.news-date{position:absolute;font-size:11px;color:var(--red)}
.news-title{position:absolute;font-family:'Oswald',sans-serif;text-transform:uppercase}
.news-link{position:absolute;font-size:11px;font-weight:600;color:var(--red);text-decoration:underline}
/* contact */
.contact-band{position:absolute;left:0;top:3677px;width:1200px;height:446px;background:linear-gradient(180deg,#2c2e32 0%,#3a3d42 60%,#2a2c30 100%);overflow:hidden}
.contact-wedge{position:absolute;right:0;top:0;width:280px;height:220px;background:var(--red);clip-path:polygon(0 0,100% 0,100% 100%)}
.form-card{position:absolute;left:100px;top:3751px;width:471px;height:459px;background:var(--red)}
.field{position:absolute;left:38px;width:398px;height:32px;background:var(--white);font-size:11px;color:var(--muted);padding:9px 12px}
.info-row{position:absolute;left:751px;display:flex;gap:14px;color:var(--white)}
.info-icon{width:30px;height:30px;border-radius:50%;background:var(--red);display:flex;align-items:center;justify-content:center;flex:none}
.info-row h5{font-family:'Oswald',sans-serif;font-weight:500;font-size:17px;text-transform:uppercase;line-height:22px}
.info-row p{font-size:12px;line-height:17px}
/* footer */
.footer-heading{position:absolute;top:4262px;font-family:'Oswald',sans-serif;font-weight:500;font-size:15px;color:var(--ink);text-transform:uppercase}
.quick-links{position:absolute;left:514px;top:4292px;list-style:none;font-size:11px;line-height:22.5px;color:var(--ink)}
.quick-links li:first-child{color:var(--red)}
.social{position:absolute;top:4340px;width:30px;height:30px;border:1.5px solid var(--muted);border-radius:50%}
</style>
</head>
<body>

<header class="site-header">
  <div class="brand" style="left:100px;top:12px;font-size:32px;line-height:40px;">VELMORA</div>
  <nav class="nav">
    <span class="active">Home</span><span>Our Story</span><span>Investment Strategy</span><span>What Sets Us Apart</span><span>Our Portfolio</span>
  </nav>
  <svg class="header-search" width="16" height="16" viewBox="0 0 16 16"><circle cx="6.5" cy="6.5" r="5" fill="none" stroke="#2f3236" stroke-width="1.6"/><line x1="10.2" y1="10.2" x2="14.5" y2="14.5" stroke="#2f3236" stroke-width="1.6"/></svg>
  <div class="header-phone">
    <svg width="13" height="13" viewBox="0 0 24 24"><path d="M6.6 10.8a15.1 15.1 0 0 0 6.6 6.6l2.2-2.2a1 1 0 0 1 1-.25 11.4 11.4 0 0 0 3.6.6 1 1 0 0 1 1 1V20a1 1 0 0 1-1 1A17 17 0 0 1 3 4a1 1 0 0 1 1-1h3.5a1 1 0 0 1 1 1c0 1.25.2 2.45.6 3.6a1 1 0 0 1-.25 1z" fill="#e21d25"/></svg>
    (555) 214-7730
  </div>
  <div class="header-cta">Contact Us</div>
</header>

<section class="hero" role="img" aria-label="City skyline with high-rise towers at sunset">
  <div class="hero-shade"></div>
  <div class="hero-wedge"></div>
  <h1 class="hero-title">
    <span>Investing in</span><br>
    <span class="hl">Communities.</span><br>
    <span>Delivering</span><br>
    <span class="hl">Lasting Value.</span>
  </h1>
  <p class="hero-copy">Velmora Partners is a vertically integrated real estate investment firm with a proven four-decade track record. We acquire, reposition, and operate high-performing assets across multiple sectors — always with a focus on exceptional, risk-adjusted returns.</p>
</section>
<div class="btn" style="left:100px;top:508px;width:158px;">Explore Our Portfolio</div>

<section class="stats">
  <div class="stat" style="left:152px;"><b>Founded 1989</b><span>Years of experience</span></div>
  <div class="stat-divider" style="left:465px;"></div>
  <div class="stat" style="left:500px;"><b>23,000+</b><span>Multifamily &amp; healthcare units</span></div>
  <div class="stat-divider" style="left:798px;"></div>
  <div class="stat" style="left:798px;"><b>$300M+</b><span>Invested in renovations</span></div>
</section>

<section class="about">
  <div class="frame-tl"></div>
  <div class="frame-br"></div>
  <div class="photo about-photo" role="img" aria-label="Team of colleagues reviewing an architectural model around a meeting table"></div>
  <h2 class="sec-title" style="left:683px;top:848px;">About Us <i class="rule"></i></h2>
  <div class="about-text">
    <p>Founded in <strong>1989</strong>, Velmora Partners is a privately held real estate investment firm specializing in the acquisition, development, and management of multifamily and healthcare properties. With a portfolio spanning <strong>23,000+ units</strong> and over <strong>$300 million</strong> invested in renovations, we deliver sustainable growth and superior returns through strategic acquisitions, hands-on asset management, and value-driven improvements.</p>
    <p>Our experienced team combines market insight with operational expertise to identify opportunities, enhance property performance, and strengthen communities. Built on integrity, vision, and results, Velmora Partners continues to lead with a proven track record of success across diverse real estate markets.</p>
  </div>
  <div class="btn" style="left:683px;top:1168px;width:145px;">Read More</div>
  <div class="ghost-word">VELMORA</div>
</section>

<section class="portfolio">
  <div class="portfolio-band"></div>
  <div class="portfolio-arrows">
    <div class="arrow-box" style="left:16px;"><svg width="10" height="10" viewBox="0 0 10 10"><path d="M6.5 1.5 3 5l3.5 3.5" fill="none" stroke="#e21d25" stroke-width="1.8"/></svg></div>
    <div class="arrow-box" style="left:56px;"><svg width="10" height="10" viewBox="0 0 10 10"><path d="M3.5 1.5 7 5 3.5 8.5" fill="none" stroke="#e21d25" stroke-width="1.8"/></svg></div>
  </div>
  <h2 class="sec-title" style="left:100px;top:1378px;color:#fff;">Our Portfolio <i class="rule" style="background:#fff;"></i></h2>
  <p class="portfolio-copy">Our experienced team combines market insight with operational expertise to identify opportunities, enhance property performance, and strengthen communities</p>
  <div class="btn" style="left:100px;top:1527px;width:145px;">View More</div>

  <div class="photo card-photo" style="left:521px;width:256px;background:linear-gradient(180deg,#8fb8dc 0%,#d9d2c8 45%,#b9a79a 70%,#2f9fb5 85%,#1f8aa3 100%);" role="img" aria-label="Waterfront apartment building with red roofs"></div>
  <div class="photo card-photo" style="left:790px;width:256px;background:linear-gradient(180deg,#9fb7c9 0%,#6f7d8a 40%,#4f5c68 75%,#59656f 100%);" role="img" aria-label="Glass residential towers against a pale sky"></div>
  <div class="photo card-photo" style="left:1059px;width:141px;background:linear-gradient(180deg,#3f86d4 0%,#8a7a66 45%,#b0862e 70%,#5f7a3a 100%);" role="img" aria-label="Apartment tower behind autumn trees"></div>
  <div class="card-cap" style="left:521px;">Riverbend Care Center<br>— Trenton, NJ</div>
  <div class="card-cap" style="left:790px;">Harborline Residences<br>— Philadelphia, PA</div>
  <div class="card-cap" style="left:1059px;">Elmwood Apartments<br>— Baltimore, MD</div>
</section>

<section class="approach">
  <h2 class="sec-title center" style="top:1823px;"><i class="rule"></i>Our Investment Approach<i class="rule"></i></h2>
  <div class="approach-col" style="left:117px;">
    <svg width="66" height="66" viewBox="0 0 66 66"><rect x="8" y="6" width="34" height="44" rx="2" fill="#e21d25"/><rect x="14" y="14" width="20" height="3" fill="#fff"/><rect x="14" y="21" width="16" height="3" fill="#fff"/><rect x="14" y="28" width="12" height="3" fill="#fff"/><circle cx="40" cy="40" r="12" fill="#fff" stroke="#e21d25" stroke-width="4"/><line x1="49" y1="49" x2="60" y2="60" stroke="#e21d25" stroke-width="6" stroke-linecap="round"/></svg>
    <h3>Identify Opportunities</h3>
    <p>Pinpoint high-potential assets through data-driven research and decades of industry expertise.</p>
  </div>
  <div class="approach-col" style="left:456px;">
    <svg width="66" height="66" viewBox="0 0 66 66"><path d="M33 10 12 28h6v30h30V28h6z" fill="#e21d25"/><text x="33" y="50" text-anchor="middle" font-family="Montserrat,sans-serif" font-weight="700" font-size="18" fill="#fff">$</text><path d="M44 14 54 4M54 4h-7M54 4v7" stroke="#e21d25" stroke-width="3" fill="none"/></svg>
    <h3>Maximize Value</h3>
    <p>Execute targeted renovations and operational enhancements that boost performance and returns.</p>
  </div>
  <div class="approach-col" style="left:793px;">
    <svg width="66" height="66" viewBox="0 0 66 66"><circle cx="20" cy="18" r="7" fill="#e21d25"/><circle cx="46" cy="18" r="7" fill="#e21d25"/><circle cx="33" cy="28" r="7" fill="#e21d25"/><path d="M8 44c0-8 5-14 12-14s12 6 12 14zM34 44c0-8 5-14 12-14s12 6 12 14z" fill="#e21d25"/><path d="M19 58c0-9 6-16 14-16s14 7 14 16z" fill="#e21d25" stroke="#fff" stroke-width="2"/></svg>
    <h3>Strengthen Communities</h3>
    <p>Foster vibrant, sustainable communities through quality improvements and responsible management.</p>
  </div>
  <div class="btn" style="left:481px;top:2108px;width:240px;">Learn More About Our Approach</div>
</section>

<section class="pillars">
  <div class="photo pillar" style="left:0;width:400px;background:linear-gradient(180deg,#b9bcc0 0%,#7f8a94 40%,#3c4147 80%,#26292d 100%);" role="img" aria-label="Laptop and financial bar chart on a desk"></div>
  <div class="photo pillar" style="left:402px;width:400px;background:linear-gradient(180deg,#c8cacc 0%,#8e9194 40%,#43464a 80%,#26292d 100%);" role="img" aria-label="Business professionals shaking hands in an office"></div>
  <div class="photo pillar" style="left:804px;width:396px;background:linear-gradient(180deg,#aab8c6 0%,#8e9aa4 35%,#4e5860 75%,#25292d 100%);" role="img" aria-label="Dense city skyline of residential towers"></div>
  <div class="pillar-cap" style="left:0;"><h4>Proven Track Record</h4><p>35+ years of success managing diverse<br>real estate assets across the U.S.</p><i></i></div>
  <div class="pillar-cap" style="left:402px;"><h4>Hands-On Management</h4><p>Active oversight ensures every property<br>meets our high performance and quality.</p><i></i></div>
  <div class="pillar-cap" style="left:802px;"><h4>Commitment to Communities</h4><p>We invest in ways that improve lives,<br>strengthen neighborhoods,</p><i></i></div>
</section>

<section class="partners" aria-label="Partner badges">
  <div class="badge" style="left:100px;"><div class="mark sq"></div><div class="bar"></div></div>
  <div class="badge" style="left:250px;"><div class="mark"></div><div class="bar"></div></div>
  <div class="badge" style="left:402px;"><div class="mark sq"></div><div class="bar"></div></div>
  <div class="badge" style="left:554px;"><div class="mark"></div><div class="bar"></div></div>
  <div class="badge" style="left:704px;"><div class="mark sq"></div><div class="bar"></div></div>
  <div class="badge" style="left:858px;"><div class="mark"></div><div class="bar"></div></div>
  <div class="badge" style="left:1015px;"><div class="mark sq"></div><div class="bar"></div></div>
</section>

<section class="news">
  <h2 class="sec-title center" style="top:2936px;"><i class="rule"></i>Our Latest News<i class="rule"></i></h2>
  <div class="news-date" style="left:100px;top:3033px;">25 June, 2025</div>
  <div class="news-title" style="left:100px;top:3064px;width:440px;font-size:25px;line-height:33px;font-weight:500;color:var(--red);">Mid-Year Outlook: Global Shocks Provide Generational Opportunity For Those Who Know Where To Look</div>
  <p class="abs" style="left:100px;top:3165px;width:330px;font-size:12px;line-height:19px;color:var(--text);">Our experienced team combines market insight with operational expertise to identify opportunities, enhance property performance, and strengthen communities. Built on integrity,</p>
  <div class="news-link" style="left:100px;top:3260px;">Learn More</div>
  <div class="abs" style="left:578px;top:3031px;width:507px;height:314px;background:var(--red);"></div>
  <div class="photo" style="left:587px;top:3040px;width:489px;height:296px;background:linear-gradient(135deg,#eeeae4 0%,#d9d3ca 45%,#b89978 70%,#e5e2dd 100%);" role="img" aria-label="Couple reviewing floor plans in a bright empty room"></div>

  <div class="abs" style="left:100px;top:3389px;width:1000px;height:1px;background:var(--line);"></div>
  <div class="news-date" style="left:100px;top:3410px;">25 June, 2025</div>
  <div class="news-title" style="left:100px;top:3437px;width:300px;font-size:14px;line-height:22px;color:var(--ink);">Lorem ipsum has been the industry's standard dummy text ever since the 1500s, type and scrambled it to specimen book.</div>
  <div class="news-link" style="left:100px;top:3513px;">Learn More</div>
  <div class="photo" style="left:419px;top:3414px;width:171px;height:124px;background:linear-gradient(135deg,#e8e6e3 0%,#c9c4bd 50%,#8d7c6b 100%);" role="img" aria-label="Hands signing a contract beside a small house model"></div>
  <div class="news-date" style="left:610px;top:3410px;">25 June, 2025</div>
  <div class="news-title" style="left:610px;top:3437px;width:300px;font-size:14px;line-height:22px;color:var(--ink);">Lorem ipsum has been the industry's standard dummy text ever since the 1500s, type and scrambled it to specimen book.</div>
  <div class="news-link" style="left:610px;top:3513px;">Learn More</div>
  <div class="photo" style="left:926px;top:3414px;width:174px;height:124px;background:linear-gradient(180deg,#8fb0cf 0%,#6d7f8c 45%,#5a7a4a 80%,#466136 100%);" role="img" aria-label="Aerial view of city towers and parkland"></div>
  <div class="btn" style="left:522px;top:3570px;width:156px;">View More News</div>
</section>

<section class="contact">
  <div class="contact-band" role="img" aria-label="Dim city skyline at dusk">
    <div class="contact-wedge"></div>
  </div>
  <div class="form-card">
    <h2 class="head-font" style="position:absolute;left:38px;top:30px;font-size:40px;font-weight:500;color:#fff;line-height:50px;">Get In Touch</h2>
    <div class="field" style="top:97px;">Name</div>
    <div class="field" style="top:143px;">Email</div>
    <div class="field" style="top:189px;">Phone</div>
    <div class="field" style="top:235px;">Select Service</div>
    <div class="field" style="top:281px;height:74px;">Messages</div>
    <div class="btn" style="left:38px;top:389px;width:112px;">Submit</div>
  </div>
  <div class="brand" style="left:751px;top:3790px;font-size:48px;line-height:56px;color:#fff;">VELMORA</div>
  <div class="info-row" style="top:3867px;">
    <div class="info-icon"><svg width="14" height="14" viewBox="0 0 24 24"><path d="M6.6 10.8a15.1 15.1 0 0 0 6.6 6.6l2.2-2.2a1 1 0 0 1 1-.25 11.4 11.4 0 0 0 3.6.6 1 1 0 0 1 1 1V20a1 1 0 0 1-1 1A17 17 0 0 1 3 4a1 1 0 0 1 1-1h3.5a1 1 0 0 1 1 1c0 1.25.2 2.45.6 3.6a1 1 0 0 1-.25 1z" fill="#fff"/></svg></div>
    <div><h5>Call Now</h5><h5 style="font-size:19px;">(555) 214-7730</h5></div>
  </div>
  <div class="info-row" style="top:3938px;">
    <div class="info-icon"><svg width="14" height="14" viewBox="0 0 24 24"><rect x="2" y="5" width="20" height="14" rx="1.5" fill="#fff"/><path d="M2.5 6 12 13l9.5-7" fill="none" stroke="#e21d25" stroke-width="1.8"/></svg></div>
    <div><h5>Email Now</h5><p>info@velmora-partners.com</p></div>
  </div>
  <div class="info-row" style="top:3996px;">
    <div class="info-icon"><svg width="14" height="14" viewBox="0 0 24 24"><path d="M12 2a7 7 0 0 0-7 7c0 5 7 13 7 13s7-8 7-13a7 7 0 0 0-7-7z" fill="#fff"/><circle cx="12" cy="9" r="2.6" fill="#e21d25"/></svg></div>
    <div><h5>Address</h5><p>240 Harbor Ave, Oakfield,<br>NJ 07012</p></div>
  </div>
</section>

<footer class="site-footer">
  <div class="brand" style="left:100px;top:4256px;font-size:58px;line-height:66px;">VELMORA</div>
  <div class="social" style="left:132px;"></div>
  <div class="social" style="left:171px;"></div>
  <div class="social" style="left:210px;"></div>
  <div class="social" style="left:249px;"></div>

  <div class="footer-heading" style="left:514px;">Quick Links</div>
  <ul class="quick-links">
    <li>Home</li><li>Our Story</li><li>Investment Strategy</li><li>What Sets Us Apart</li><li>Our Portfolio</li><li>Contact Us</li>
  </ul>

  <div class="footer-heading" style="left:845px;">Subscribe Newsletter</div>
  <div class="abs" style="left:845px;top:4298px;width:255px;height:31px;border:1px solid #bfc1c4;font-size:10px;color:var(--muted);padding:9px 12px;">Email</div>
  <div class="abs" style="left:845px;top:4345px;width:255px;height:32px;background:var(--red);color:#fff;font-size:11px;font-weight:600;display:flex;align-items:center;justify-content:center;box-shadow:3px 3px 0 #b5141b;">Subscribe Now</div>

  <div class="abs" style="left:100px;top:4451px;width:1000px;height:1px;background:var(--line);"></div>
  <div class="abs" style="left:0;top:4471px;width:1200px;text-align:center;font-size:11px;color:var(--text);">© Copyright All Right Reserved 2025</div>
</footer>

</body>
</html>
```